Luxury Travel Agency needs a website

We are in need of a website design for a luxury travel agency that specializes in Marlowe travel. The name of the owner's company is Brightwell Voyages. This website will need a blog section, as the owner will be posting content on the website weekly. The website also needs a page for a contact form.

We want to see a design that is inspired by Marlowe's Royal Tidewater. Images of the owner's company logo and Marlowes's Royal Tidewater will be uploaded below.

Please be mindful that the owner is selling luxury travel and wants a website that communicates luxury and premium service.

Target Market(s)

35-60 year old professional woman, married with children, homeowner, $500,000 total household income

Industry/Entity Type

Luxury Travel

Coding

Number of Pages Required

3 page

Font styles to use
Decorative

Colors
0094D4
00A9DD
6FCCEA
C7EBF8
E9F6FB
E54698
E96AAD
F1A4CE
F9D9EA
FCEFF6

Requirements
Must have
• Premium, high-end luxury design. It must have a home page, contact page, and blog page
Nice to have
• One of a kind design, no boring and cheap templates
Should not have
• Cheap design

```html
<!DOCTYPE html>
<html lang="en">
<head>
<meta charset="utf-8">
<title>Brightwell Voyages</title>
<link href="https://fonts.googleapis.com/css2?family=Abril+Fatface&family=Mulish:wght@400;600;700;800&display=swap" rel="stylesheet">
<style>
:root{
  --blue:#0094D4;
  --blue-2:#00A9DD;
  --blue-3:#6FCCEA;
  --blue-4:#C7EBF8;
  --blue-5:#E9F6FB;
  --pink:#E54698;
  --pink-2:#E96AAD;
  --pink-3:#F1A4CE;
  --pink-4:#F9D9EA;
  --pink-5:#FCEFF6;
  --frame:#A9CFD3;
  --ink:#3a3a44;
  --dark:#2b2b2f;
  --white:#ffffff;
}
*{box-sizing:border-box;margin:0;padding:0}
html,body{width:1200px;height:3689px;overflow:hidden;background:var(--white)}
body{font-family:"Mulish",sans-serif;color:var(--ink);position:relative}
a{text-decoration:none;color:inherit}
.abs{position:absolute}
.display{font-family:"Abril Fatface",serif;font-weight:400}
.frame{position:absolute;border:2px solid var(--frame);border-radius:6px;background:var(--white)}
.btn{position:absolute;background:var(--pink);color:var(--white);font-weight:800;font-size:14px;letter-spacing:.3px;display:flex;align-items:center;justify-content:center;gap:10px;text-transform:uppercase}
.photo{position:absolute}
.brand{font-weight:800;color:var(--pink);font-size:25px;letter-spacing:.5px}

/* header */
.logo{left:129px;top:34px;display:flex;align-items:center;gap:10px}
.logo .dot{width:18px;height:18px;border-radius:50%;background:var(--blue-3)}
.nav{left:487px;top:23px;width:418px;height:64px;display:flex;align-items:center;justify-content:center}
.nav a{font-size:14.5px;color:var(--ink);padding:0 19px;border-right:1px solid #cfd8da;text-transform:uppercase}
.nav a:last-child{border-right:0}
.nav a.active{color:var(--pink)}
.follow{left:935px;top:37px;display:flex;align-items:center;gap:10px;font-size:12px}
.follow .line{border-top:1px solid #ccc;border-bottom:1px solid #ccc;padding:5px 0}
.sq{width:30px;height:30px;border-radius:5px}

/* hero */
.hero{left:0;top:115px;width:1200px;height:597px;background:linear-gradient(180deg,#e9eef2 0%,#f2f3f1 35%,#d6d9d4 62%,#6f8f4d 88%,#5b7b3a 100%)}
.welcome{left:129px;top:626px;width:939px;height:86px;background:rgba(233,246,251,.93);display:flex;align-items:center}
.welcome h1{font-size:22px;line-height:27px;width:210px;margin-left:33px;color:var(--blue)}
.welcome h1 span{color:var(--pink);display:block}
.welcome .sep{width:2px;height:48px;background:var(--blue);margin:0 30px 0 14px}
.welcome p{font-size:13px;line-height:16px;width:420px;color:var(--ink)}
.welcome .btn{left:760px;top:24px;width:155px;height:40px}

/* tiles */
.tile-link{position:absolute;top:1057px;width:246px;height:43px;display:flex;align-items:center;justify-content:center;gap:8px;font-size:13.5px}
.tile-link .ico{width:17px;height:17px;border-radius:50%}
.tile-link .beads{color:var(--pink-3);letter-spacing:1px;font-size:11px}

/* about */
.about-band{left:0;top:1153px;width:1200px;height:508px;background:linear-gradient(90deg,#eef5f8,#e6f1f5)}
.section-title{display:flex;align-items:center;justify-content:center;font-size:26px;color:var(--blue)}
.section-title span{color:var(--pink);margin-left:8px}
.body-text{font-size:14px;line-height:22.5px;text-align:justify}
.body-text p+p{margin-top:22px}

/* posts */
.card{position:absolute;top:1816px;width:297px;height:432px;border:1px solid var(--blue-3);background:var(--white)}
.card .img{position:absolute;left:0;top:0;width:100%;height:202px}
.card .date{position:absolute;left:28px;top:232px;font-size:11px;text-transform:uppercase}
.card h3{position:absolute;left:28px;top:258px;width:230px;font-weight:600;font-size:16px;line-height:21px;color:var(--dark)}
.card p{position:absolute;left:28px;top:333px;width:240px;font-size:11px;line-height:16px}
.card .btn{left:29px;top:377px;width:84px;height:28px;font-size:9px}
.arrow{position:absolute;top:2017px;width:24px;height:24px;border:2px solid var(--blue);border-radius:6px;display:flex;align-items:center;justify-content:center}

/* what we do */
.do-band{left:0;top:2308px;width:1200px;height:560px;background:var(--blue-5)}

/* subscribe */
.sub-card{left:308px;top:2947px;width:759px;height:315px;background:var(--white);box-shadow:0 8px 30px rgba(0,0,0,.08)}
.input{position:absolute;left:112px;top:153px;width:439px;height:51px;border:2px solid var(--blue);display:flex;align-items:center;gap:10px;padding-left:20px;font-size:14px;color:#777}

/* footer */
.footer{left:0;top:3337px;width:1200px;height:352px;background:var(--dark);color:#e8e8e8}
.footer h4{font-family:"Abril Fatface",serif;font-weight:400;font-size:19px;color:var(--white)}
.footer p,.footer li{font-size:12.5px;line-height:19px}
.footer ul{list-style:none}
.footer li{margin-bottom:10px}
.rule{left:130px;width:940px;height:1px;background:#555}
</style>
</head>
<body>

<header>
  <div class="abs logo"><span class="dot"></span><span class="brand">Brightwell Voyages</span></div>
  <nav class="frame nav">
    <a class="active" href="#">Home</a><a href="#">About</a><a href="#">Blog</a><a href="#">Contact us</a>
  </nav>
  <div class="abs follow"><span class="line">FOLLOW</span><span class="sq" style="background:#3b5998"></span><span class="sq" style="background:var(--pink-2)"></span></div>
</header>

<section>
  <div class="photo hero abs" role="img" aria-label="Grand white Victorian resort hotel with red roofs, palm trees and a fountain in front"></div>
  <div class="abs welcome">
    <h1 class="display">Welcome to <span>Brightwell Voyages</span></h1>
    <div class="sep"></div>
    <p>We are currently living in an ever-changing environment. Having a professional in your corner which can assist you at a moment's notice is priceless.</p>
    <a class="btn" href="#"><svg width="16" height="12" viewBox="0 0 16 12"><rect x="1" y="1" width="14" height="10" fill="none" stroke="#fff" stroke-width="1.5"/><path d="M1 1l7 6 7-6" fill="none" stroke="#fff" stroke-width="1.5"/></svg>Contact us</a>
  </div>
</section>

<section>
  <div class="photo" style="left:130px;top:765px;width:302px;height:266px;background:linear-gradient(135deg,#f3ece0,#e7d9bd 60%,#c9b38a)" role="img" aria-label="Travel agent standing beside a vintage casting agency sign at the park"></div>
  <div class="photo" style="left:448px;top:765px;width:304px;height:266px;background:linear-gradient(180deg,#bcd7ee 0%,#9fc3e3 45%,#7c92b7 80%,#4c5d7d)" role="img" aria-label="Fairytale castle with blue spires under a bright sky"></div>
  <div class="photo" style="left:768px;top:765px;width:300px;height:266px;background:linear-gradient(180deg,#f1e6c9,#d8c08a 55%,#7c6b3f)" role="img" aria-label="Hotel lobby with a grand chandelier and balconies"></div>

  <div class="frame tile-link" style="left:165px"><span class="ico" style="background:var(--blue)"></span>Friendly <span class="beads">•••••</span>›</div>
  <div class="frame tile-link" style="left:484px"><span class="ico" style="background:var(--blue-2)"></span>Snapline <span class="beads">•••••</span>›</div>
  <div class="frame tile-link" style="left:803px"><span class="ico" style="background:var(--blue)"></span>Get in touch <span class="beads">•••••</span>›</div>
</section>

<section>
  <div class="abs about-band"></div>
  <div class="frame section-title display" style="left:130px;top:1212px;width:415px;height:58px">About <span>Brightwell Voyages</span></div>
  <div class="abs body-text" style="left:132px;top:1312px;width:448px">
    <p>My name is Clara, and I am the founder of Brightwell Voyages. Brightwell Voyages was born out of my innate love of Marlowe. After working as a cast member from 2013-2014, many friends and family would ask me for advice on booking and planning their Marlowe vacation.</p>
    <p>Fast forward to fall 2020, when I began planning our Christmas Marlowe vacation for that year. There were many unknowns traveling to Marlowe and what to expect upon arrival. I read as much information as possible; however, that gave me more unanswered questions than answers.</p>
  </div>
  <a class="btn" href="#" style="left:135px;top:1568px;width:123px;height:43px">Read more</a>
  <div class="photo" style="left:652px;top:1188px;width:358px;height:473px;background:linear-gradient(180deg,#e9eef2,#d6c3b4 50%,#1f2a44)" role="img" aria-label="Portrait of the agency founder wearing polka-dot ears"></div>
</section>

<section>
  <div class="frame section-title display" style="left:468px;top:1713px;width:263px;height:60px">Recent <span>Posts</span></div>

  <div class="arrow" style="left:70px"><svg width="12" height="12" viewBox="0 0 12 12"><path d="M11 6H2M6 2L2 6l4 4" fill="none" stroke="#0094D4" stroke-width="1.8"/></svg></div>
  <div class="arrow" style="left:1102px"><svg width="12" height="12" viewBox="0 0 12 12"><path d="M1 6h9M6 2l4 4-4 4" fill="none" stroke="#0094D4" stroke-width="1.8"/></svg></div>

  <article class="card" style="left:130px">
    <div class="img" style="background:linear-gradient(180deg,#1d3a7a,#6a4aa0 55%,#1a1c30)" role="img" aria-label="Castle lit in purple at dusk"></div>
    <div class="date">October 29, 2021</div>
    <h3>Recruiting a Marlowe Travel Agent Creates Winner Vacations</h3>
    <p>Lorem Ipsum is simply dummy text of the printing and typesetting industry.</p>
    <a class="btn" href="#">Read more</a>
  </article>
  <article class="card" style="left:451px">
    <div class="img" style="background:radial-gradient(circle at 50% 50%,#c9a850 0%,#6b5a2e 45%,#3d4c68 75%)" role="img" aria-label="Ornate gold framed resort sign"></div>
    <div class="date">October 29, 2021</div>
    <h3>Staying at a Marlowe World hotel? How Long To Really Stay</h3>
    <p>Lorem Ipsum is simply dummy text of the printing and typesetting industry.</p>
    <a class="btn" href="#">Read more</a>
  </article>
  <article class="card" style="left:770px">
    <div class="img" style="background:linear-gradient(180deg,#f4ecdc,#e0ceae 55%,#6e5a42)" role="img" aria-label="Grand lobby with a piano and palm trees"></div>
    <div class="date">October 29, 2021</div>
    <h3>Which Marlowe Value Resort is best?</h3>
    <p>Lorem Ipsum is simply dummy text of the printing and typesetting industry.</p>
    <a class="btn" href="#">Read more</a>
  </article>
</section>

<section>
  <div class="abs do-band"></div>
  <div class="photo" style="left:132px;top:2308px;width:425px;height:560px;background:linear-gradient(180deg,#f3eee3,#e2d6bd 45%,#b9a57e 75%,#4c5c3c)" role="img" aria-label="Lobby atrium with stained glass dome, chandelier and live band"></div>
  <div class="frame section-title display" style="left:594px;top:2354px;width:260px;height:60px">What <span>We Do</span></div>
  <div class="abs body-text" style="left:594px;top:2444px;width:476px">
    <p>Marlowe Travel Agents at Brightwell Voyages do all the heavy lifting and research for you while planning your dream Marlowe Vacation. You can do as much or as little planning as you like. Want someone to plan every detail of your trip from flights to transportation and more? We've got you covered.</p>
    <p>Know you want to plan a few things but want someone else to get it all packaged for you? We are here to do that as well. Even if you are a seasoned Marlowe veteran having a travel advisor in your corner can help you in various ways. We are currently living in an ever-changing environment.</p>
    <p>Having a professional in your corner which can assist you at a moment's notice is priceless.</p>
  </div>
  <a class="btn" href="#" style="left:597px;top:2782px;width:155px;height:42px"><svg width="16" height="12" viewBox="0 0 16 12"><rect x="1" y="1" width="14" height="10" fill="none" stroke="#fff" stroke-width="1.5"/><path d="M1 1l7 6 7-6" fill="none" stroke="#fff" stroke-width="1.5"/></svg>Contact us</a>
</section>

<section>
  <div class="photo" style="left:132px;top:2940px;width:248px;height:342px;background:radial-gradient(ellipse at 50% 50%,var(--pink-4) 0%,var(--blue-5) 55%,rgba(255,255,255,0) 75%)" role="img" aria-label="Soft decorative monogram area in pink and teal"></div>
  <div class="abs sub-card">
    <div class="frame section-title display" style="left:110px;top:46px;width:195px;height:62px;font-size:25px">Subscribe</div>
    <p class="abs" style="left:377px;top:50px;width:280px;font-size:13.5px;line-height:22px">Sign up to our newsletter and stay up to date Don't worry, we won't send you too much content.</p>
    <div class="input"><svg width="18" height="13" viewBox="0 0 18 13"><rect x="1" y="1" width="16" height="11" fill="none" stroke="#0094D4" stroke-width="1.5"/><path d="M1 1l8 6 8-6" fill="none" stroke="#0094D4" stroke-width="1.5"/></svg>Email</div>
    <a class="btn" href="#" style="left:565px;top:153px;width:152px;height:51px;font-size:16px">Subscribe</a>
    <p class="abs" style="left:112px;top:228px;width:480px;font-size:12px;line-height:19px">By submitting your information, you are granting us permission to email you. You may unsubscribe at any time</p>
  </div>
</section>

<footer class="abs footer">
  <div class="abs" style="left:130px;top:52px;width:300px">
    <h4>About Brightwell</h4>
    <p style="margin-top:12px">Brightwell Voyages is an independent affiliate of Harborline LLC</p>
    <p style="margin-top:18px">This is a personal blog and is in no way affiliated with the Marlowe Parks Company. All opinions expressed are my own. Please visit marloweparks.com for official information concerning Marlowe.</p>
  </div>
  <div class="abs" style="left:509px;top:52px">
    <h4>Quick Links</h4>
    <ul style="margin-top:14px"><li>Home</li><li>About</li><li>Blog</li><li>Contact us</li></ul>
  </div>
  <div class="abs" style="left:776px;top:52px;display:flex;align-items:center;gap:14px">
    <h4>Follow us</h4>
    <span class="sq" style="background:#3b5998;width:28px;height:28px"></span>
    <span class="sq" style="background:var(--pink-2);width:28px;height:28px"></span>
    <span class="sq" style="background:var(--blue-2);width:28px;height:28px;border-radius:50%"></span>
  </div>
  <div class="abs" style="left:745px;top:140px;display:flex;align-items:center;gap:12px">
    <span style="width:20px;height:20px;border-radius:50%;background:var(--blue-3)"></span>
    <span style="font-weight:800;font-size:32px;color:var(--pink-3)">Brightwell Voyages</span>
  </div>
  <div class="abs rule" style="top:253px"></div>
  <div class="abs rule" style="top:258px"></div>
  <p class="abs" style="left:0;top:300px;width:1200px;text-align:center;font-size:12.5px">© 2021 Brightwell Voyages</p>
</footer>

</body>
</html>
```